Private Gym Needs a Rack Card Design

We need a basic front and back rack card (same size as post card) that gives basic information about our brand, and includes our logo. Please see attached logo and required content below.

Target Market(s)

Upscale, private gym.

Industry/Entity Type

Gym

Font styles to use
Sans Serif

Colors
ffffff
5c5c5c
000000
dbdbdb
f78f20

Requirements
Must have
• Business Logo and the following text in a clean, modern, easy-to-read, artistic manner. Style and design must be clean, incorporate our color scheme of MOSTLY white, light grey, charcoal, with just pops of orange. We want the card itself to be mostly white background. Must include website URL as well: corevantagestudio.com
• FRONT CARD:
• Logo
• A safe and individualized approach to exercise
• Our method employs the latest weight resistance training exercises and coaching for healthy living. Not only is our workout methodology effective, it’s safe.
• Our Method…
• -Improves Functional Movement
• -Promotes Weight Loss
• -Builds Strength
• -Increases Flexibility 

• BACK:
• Change Your Body. Find Your Strength.
• There’s 40 years of success behind our proven method
• What is The Formwell? 
• The Formwell is all about teaching our clients how to lift weights and exercise with the proper technique. There’s no slinging or jerking at our gym; only controlled movements that yield real results.
• Come workout with us in our private gym. We are located in Durham adjacent to Harlow Campus and 5 minutes from downtown Durham.
• Address: 482 Linden Ave, Durham, NC 27705
• Phone: (919) 555-2741
• Hours: 9:00 AM – 9:00 PM
Nice to have
• Great organization of text, maybe some columns, colored bullet points, cool graphics and logos.
Should not have
• Busy or crowded design. All lines should be sleek, straight, and streamline. NO STOCK IMAGES, but logos are GREAT

```html
<!DOCTYPE html>
<html lang="en">
<head>
<meta charset="utf-8">
<title>The Formwell – Rack Card</title>
<link href="https://fonts.googleapis.com/css2?family=Open+Sans:wght@400;600;700;800&display=swap" rel="stylesheet">
<style>
  :root {
    --orange: #f26a36;
    --charcoal: #5c5c5c;
    --light: #dbdbdb;
    --faint: #ececec;
    --white: #ffffff;
    --page: #e6e6e6;
    --ink: #4a4a4a;
  }
  * { box-sizing: border-box; margin: 0; padding: 0; }
  html, body {
    width: 1200px; height: 1000px; overflow: hidden;
    background: var(--page);
    font-family: "Open Sans", Arial, sans-serif;
  }
  .card {
    position: absolute; left: 255px;
    width: 690px; height: 470px;
    background: var(--white);
    overflow: hidden;
    box-shadow: 0 2px 8px rgba(0,0,0,.15);
  }
  .card--front { top: 20px; }
  .card--back { top: 510px; }
  .card__art { position: absolute; inset: 0; width: 100%; height: 100%; }

  .brand {
    position: absolute;
    font-weight: 800; color: var(--charcoal);
    font-size: 42px; letter-spacing: -0.5px; line-height: 1;
    display: flex; align-items: center; gap: 10px;
  }
  .brand__mark { width: 14px; height: 14px; background: var(--orange); }

  /* Front */
  .card--front .brand { left: 95px; top: 90px; }
  .front__tagline {
    position: absolute; left: 52px; top: 180px;
    color: var(--orange); font-size: 18px;
  }
  .front__intro {
    position: absolute; left: 52px; top: 242px; width: 340px;
    color: var(--white); font-size: 15px; line-height: 30px;
  }
  .front__intro b { font-weight: 700; }
  .benefits {
    position: absolute; left: 400px; top: 244px;
    list-style: none; color: var(--white); font-size: 15.5px;
  }
  .benefits li { line-height: 29px; display: flex; align-items: center; gap: 6px; }
  .benefits svg { width: 13px; height: 13px; flex: none; }
  .front__url {
    position: absolute; left: 78px; top: 396px;
    color: var(--charcoal); font-size: 18px; letter-spacing: 5px;
  }

  /* Back */
  .card--back .brand { left: 262px; top: 50px; width: 405px; justify-content: center; }
  .slogans {
    position: absolute; left: 20px; top: 190px; width: 222px;
    list-style: none; color: var(--white); font-weight: 700; font-size: 17px; line-height: 23px;
  }
  .slogans li { display: flex; gap: 8px; margin-bottom: 24px; }
  .slogans svg { width: 22px; height: 14px; flex: none; margin-top: 4px; }
  .about__title {
    position: absolute; left: 262px; top: 158px; width: 405px; text-align: center;
    color: var(--orange); font-weight: 700; font-size: 22px; letter-spacing: 1px;
  }
  .about__list {
    position: absolute; left: 250px; top: 200px; width: 420px;
    list-style: none; color: var(--ink); font-size: 14.5px; line-height: 19px; letter-spacing: .4px;
  }
  .about__list li { display: flex; gap: 10px; margin-bottom: 10px; }
  .about__bullet { width: 16px; height: 6px; background: var(--orange); margin-top: 8px; flex: none; }
  .contact {
    position: absolute; left: 0; top: 404px; width: 690px; height: 50px;
    background: var(--charcoal); color: var(--white);
    font-size: 14.5px; line-height: 21px; letter-spacing: 1px;
    display: flex; padding: 4px 40px 0 42px; justify-content: space-between;
  }
</style>
</head>
<body>

<!-- Front of rack card -->
<section class="card card--front">
  <svg class="card__art" viewBox="0 0 690 470" aria-hidden="true">
    <polygon points="520,0 690,0 690,215 520,215" fill="var(--orange)"/>
    <polygon points="360,0 440,0 560,215 480,215" fill="var(--faint)"/>
    <polygon points="440,0 475,0 590,215 560,215" fill="var(--light)"/>
    <polygon points="475,0 535,0 600,215 575,215" fill="var(--charcoal)"/>
    <polygon points="600,215 640,215 690,100 690,20" fill="var(--light)"/>
    <polygon points="645,215 665,215 690,160 690,120" fill="var(--charcoal)"/>
    <polygon points="0,215 690,215 690,385 0,385" fill="var(--orange)"/>
    <polygon points="470,385 540,385 580,470 510,470" fill="var(--faint)"/>
    <polygon points="600,385 690,385 690,470 560,470" fill="var(--orange)"/>
    <polygon points="570,385 610,385 570,470 530,470" fill="var(--charcoal)"/>
  </svg>
  <div class="brand"><span class="brand__mark"></span>The Formwell</div>
  <p class="front__tagline">A safe and individualized approach to exercise.</p>
  <p class="front__intro"><b>O</b>ur method employs the latest weight resistance training exercises and coaching for healthy living. Not only is our workout methodology effective, it’s safe.</p>
  <ul class="benefits">
    <li><svg viewBox="0 0 12 12"><path d="M1 6.5 4.5 10 11 2" fill="none" stroke="#fff" stroke-width="2.4"/></svg>Builds Strength</li>
    <li><svg viewBox="0 0 12 12"><path d="M1 6.5 4.5 10 11 2" fill="none" stroke="#fff" stroke-width="2.4"/></svg>Increases Flexibility</li>
    <li><svg viewBox="0 0 12 12"><path d="M1 6.5 4.5 10 11 2" fill="none" stroke="#fff" stroke-width="2.4"/></svg>Promotes Weight Loss</li>
    <li><svg viewBox="0 0 12 12"><path d="M1 6.5 4.5 10 11 2" fill="none" stroke="#fff" stroke-width="2.4"/></svg>Improves Functional Movement</li>
  </ul>
  <p class="front__url">www.corevantagestudio.com</p>
</section>

<!-- Back of rack card -->
<section class="card card--back">
  <svg class="card__art" viewBox="0 0 690 470" aria-hidden="true">
    <polygon points="0,0 45,0 45,470 0,470" fill="var(--orange)"/>
    <polygon points="120,0 170,0 350,470 300,470" fill="var(--faint)"/>
    <polygon points="80,0 120,0 300,470 260,470" fill="var(--light)"/>
    <polygon points="45,0 80,0 260,470 225,470" fill="var(--charcoal)"/>
    <rect x="10" y="165" width="235" height="205" fill="var(--orange)"/>
  </svg>
  <div class="brand"><span class="brand__mark"></span>The Formwell</div>
  <ul class="slogans">
    <li><svg viewBox="0 0 22 14"><path d="M0 0 22 7 0 14 6 7Z" fill="#fff"/></svg>Change Your Body, Find Your Strength</li>
    <li><svg viewBox="0 0 22 14"><path d="M0 0 22 7 0 14 6 7Z" fill="#fff"/></svg>There is 40 years of success behind our proven method</li>
  </ul>
  <h2 class="about__title">What is The Formwell?</h2>
  <ul class="about__list">
    <li><span class="about__bullet"></span>The Formwell is all about teaching our clients how to lift weights and exercise with the proper technique.</li>
    <li><span class="about__bullet"></span>There’s no slinging or jerking at our gym; only controlled movements that yield real results.</li>
    <li><span class="about__bullet"></span>Come workout with us in our private gym. We are located in Durham adjacent to Harlow Campus and 5 minutes from downtown Durham.</li>
  </ul>
  <div class="contact">
    <p>Address: 482 Linden Ave, Durham, NC 27705<br>Site: www.corevantagestudio.com</p>
    <p>Phone: (919) 555-2741<br>Hours: 9:00 AM – 9:00 PM</p>
  </div>
</section>

</body>
</html>
```